Kid's Cancer Camp Business Card

Create a unique Two-Sided color business cards for Camp Willow Brook, a pediatric cancer camp.

The camp tag line is: A place where kids with cancer have fun...

Dale Morrisey, Executive Director
Camp Willow Brook Charitable Foundation, Inc
PO Box 918
Branford, CT 06832

Phone - 203-555-0143
Fax - 203-555-0187
Email: dale@campwillowbrook.example
www.campwillowbrook.example

Target Market(s)

Potential Donors, Volunteers and Campers

Industry/Entity Type

Non-profit pediatric cancer camp

Contact Information for Business Card

All contact info that is included in the description

Font styles to use
Other font styles liked:
• Designer chooses font

Requirements
Must have
• Camp Willow Brook Logo and Tag Line
Nice to have
• should be eye catching
Should not have
• not cartoony

```html
<!DOCTYPE html>
<html lang="en">
<head>
<meta charset="utf-8">
<title>Camp Willow Brook – Business Card</title>
<link rel="stylesheet" href="https://fonts.googleapis.com/css2?family=Montserrat:wght@400;500;600;700&display=swap">
<style>
  :root {
    --page-bg: #e4e4e4;
    --card-blue-deep: #0a66a4;
    --card-blue-light: #5c9fcc;
    --card-white: #f3f3f3;
    --brand-blue: #2a6fa4;
    --tagline-blue: #1d68a6;
    --text-grey: #4f4f4f;
    --icon-blue: #2a6fa4;
    --sun-yellow: #fbb82e;
    --sun-gold: #e8a71c;
    --white: #ffffff;
  }
  * { margin: 0; padding: 0; box-sizing: border-box; }
  html, body {
    width: 1200px; height: 1200px; overflow: hidden;
    background: var(--page-bg);
    font-family: "Montserrat", Arial, sans-serif;
  }
  .canvas {
    width: 1200px; height: 1200px;
    display: flex; flex-direction: column; align-items: center; justify-content: space-evenly;
  }
  .card {
    position: relative;
    width: 960px; height: 549px;
    border-radius: 26px;
    overflow: hidden;
    box-shadow: 0 6px 18px rgba(0,0,0,0.18);
  }
  /* Front side */
  .card-front {
    background: linear-gradient(100deg, var(--card-blue-light) 0%, var(--card-blue-deep) 55%, var(--card-blue-deep) 100%);
    display: flex; align-items: center; justify-content: center;
  }
  .front-brand {
    display: flex; align-items: center; gap: 18px;
    color: var(--white);
    font-weight: 600; font-size: 52px; letter-spacing: 0.5px;
  }
  .brand-dot {
    width: 44px; height: 44px; border-radius: 50%;
    background: var(--sun-yellow);
  }
  /* Back side */
  .card-back { background: var(--card-white); }
  .holder {
    position: absolute; left: 82px; top: 118px;
  }
  .holder-name {
    color: var(--brand-blue);
    font-weight: 700; font-size: 48px; line-height: 1.05;
  }
  .holder-title {
    color: var(--text-grey);
    font-weight: 500; font-size: 24px; margin-top: 6px; margin-left: 12px;
  }
  .back-brand {
    position: absolute; right: 70px; top: 120px;
    display: flex; align-items: center; gap: 14px;
    color: var(--brand-blue);
    font-weight: 600; font-size: 34px;
  }
  .back-brand .brand-dot { width: 32px; height: 32px; background: var(--sun-gold); }
  .contact {
    position: absolute; left: 104px; top: 318px;
    list-style: none;
    color: var(--text-grey); font-size: 24px; font-weight: 500;
  }
  .contact li { display: flex; align-items: center; gap: 14px; height: 34px; white-space: nowrap; }
  .contact svg { width: 20px; height: 20px; fill: var(--icon-blue); flex: none; }
  .address {
    position: absolute; left: 104px; top: 462px;
    color: var(--text-grey); font-size: 24px; font-weight: 500; line-height: 1.3;
  }
  .tagline {
    position: absolute; right: 70px; top: 466px;
    color: var(--tagline-blue); font-size: 22px; font-weight: 500;
    white-space: nowrap;
  }
</style>
</head>
<body>
<main class="canvas">
  <section class="card card-front" role="img" aria-label="Blue card face with a repeating pattern of soft sun motifs">
    <div class="front-brand"><span class="brand-dot"></span>Camp Willow Brook</div>
  </section>

  <section class="card card-back">
    <div class="holder">
      <div class="holder-name">Dale Morrisey</div>
      <div class="holder-title">Executive Director</div>
    </div>

    <div class="back-brand"><span class="brand-dot"></span>Camp Willow Brook</div>

    <ul class="contact">
      <li>
        <svg viewBox="0 0 24 24"><path d="M6.6 10.8a15.1 15.1 0 0 0 6.6 6.6l2.2-2.2a1 1 0 0 1 1-.25 11.4 11.4 0 0 0 3.6.57 1 1 0 0 1 1 1V20a1 1 0 0 1-1 1A17 17 0 0 1 3 4a1 1 0 0 1 1-1h3.5a1 1 0 0 1 1 1c0 1.25.2 2.45.57 3.57a1 1 0 0 1-.25 1z"/></svg>
        203-555-0143
      </li>
      <li>
        <svg viewBox="0 0 24 24"><path d="M7 3h10v4H7zM4 8h16a2 2 0 0 1 2 2v6h-4v5H6v-5H2v-6a2 2 0 0 1 2-2zm4 8v3h8v-3z"/></svg>
        203-555-0187
      </li>
      <li>
        <svg viewBox="0 0 24 24"><path d="M2 5h20v14H2zm2 2v.5l8 5 8-5V7z"/></svg>
        dale@campwillowbrook.example
      </li>
      <li>
        <svg viewBox="0 0 24 24"><path d="M12 2a10 10 0 1 0 0 20 10 10 0 0 0 0-20zm6.9 9h-3a15 15 0 0 0-1.2-5.6A8 8 0 0 1 18.9 11zM12 4.1c.9 1.2 1.8 3.7 1.9 6.9h-3.8c.1-3.2 1-5.7 1.9-6.9zM9.3 5.4A15 15 0 0 0 8.1 11h-3a8 8 0 0 1 4.2-5.6zM5.1 13h3a15 15 0 0 0 1.2 5.6A8 8 0 0 1 5.1 13zm6.9 6.9c-.9-1.2-1.8-3.7-1.9-6.9h3.8c-.1 3.2-1 5.7-1.9 6.9zm2.7-1.3a15 15 0 0 0 1.2-5.6h3a8 8 0 0 1-4.2 5.6z"/></svg>
        www.campwillowbrook.example
      </li>
    </ul>

    <div class="address">P.O. Box 918 Branford,<br>CT 06832</div>

    <div class="tagline">A place where kids with cancer have fun...</div>
  </section>
</main>
</body>
</html>
```